Experienced Home remodel service

I'm a home remodeler. I want a catch phrase that clearly describes viewers what kind of work I'm in like the purple phrase on my rough draft idea. I need my website, phone, logo, slogan included. The picture is of my daughter. I want her on it. Be cool if something could be added to her picture like a hard hat or tool belt ect and her picture cut out/background removed. Some kind of background other than plain white for whole picture. I added extra pics of her so pick one

Target Market(s)

Home owners between 30-60

Industry/Entity Type

Home renovation/remodel

Colors

Designer to choose colors to be used in the design.

Requirements
Must have
• Daughters picture incorporated. Logo, phone, website address, slogan,
Nice to have
• See a hardhat or tool belt added to one of my daughters pictures that is chosen to use by designer

```html
<!DOCTYPE html>
<html lang="en">
<head>
<meta charset="utf-8">
<title>Harlan Home Solutions – Billboard</title>
<link rel="stylesheet" href="https://fonts.googleapis.com/css2?family=Anton&family=Outfit:wght@400;500&display=swap">
<style>
  :root {
    --page-bg: #8a8a8a;
    --ink-black: #0b0b0b;
    --slogan-white: #ffffff;
    --remodel-purple: #6a35c2;
    --phone-yellow: #f6f03c;
    --band-white: #ffffff;
    --bg-grey-light: #c9c6cc;
    --bg-grey-mid: #a9a5ad;
    --bg-lavender: #b8b3c2;
    --bg-warm: #c2b79a;
  }
  * { margin: 0; padding: 0; box-sizing: border-box; }
  html, body { width: 992px; height: 1200px; overflow: hidden; background: var(--page-bg); }
  body { position: relative; font-family: "Outfit", sans-serif; }

  .billboard {
    position: absolute;
    left: 26px; top: 365px;
    width: 940px; height: 469px;
    overflow: hidden;
    background:
      radial-gradient(ellipse 120px 200px at 430px 260px, rgba(214,196,120,0.45), transparent 70%),
      radial-gradient(ellipse 260px 180px at 150px 300px, rgba(190,178,150,0.5), transparent 70%),
      radial-gradient(ellipse 300px 200px at 780px 120px, rgba(225,222,232,0.7), transparent 70%),
      linear-gradient(180deg, var(--bg-grey-light) 0%, var(--bg-lavender) 45%, var(--bg-grey-mid) 100%);
  }

  .brand-mark {
    position: absolute;
    left: 40px; top: 120px;
    display: flex; align-items: center; gap: 8px;
    font-family: "Outfit", sans-serif;
    font-weight: 500;
    font-size: 16px;
    letter-spacing: 1px;
    color: var(--ink-black);
    white-space: nowrap;
  }
  .brand-mark .brand-square { width: 14px; height: 14px; background: var(--ink-black); }

  .company-title {
    position: absolute;
    right: 25px; top: 36px;
    font-family: "Anton", sans-serif;
    font-size: 62px;
    line-height: 1;
    color: var(--ink-black);
    letter-spacing: 0.5px;
    white-space: nowrap;
  }

  .slogan {
    position: absolute;
    left: 582px; top: 110px;
    transform: translateX(-50%);
    font-size: 27px;
    color: var(--slogan-white);
    white-space: nowrap;
  }

  .tagline {
    position: absolute;
    left: 497px; top: 182px;
    transform: translateX(-50%);
    font-size: 43px;
    line-height: 55px;
    color: var(--remodel-purple);
    text-align: center;
    white-space: nowrap;
  }

  .phone {
    position: absolute;
    left: 41px; top: 322px;
    display: flex; align-items: center; gap: 14px;
    font-family: "Outfit", sans-serif;
    font-weight: 500;
    font-size: 84px;
    line-height: 1;
    color: var(--phone-yellow);
    white-space: nowrap;
  }
  .phone svg { width: 52px; height: 52px; }

  .web-band {
    position: absolute;
    left: 0; right: 0; bottom: 0;
    height: 49px;
    background: var(--band-white);
  }
  .website {
    position: absolute;
    left: 58px; top: 6px;
    display: flex; align-items: center; gap: 30px;
    font-size: 32px;
    line-height: 36px;
    color: var(--ink-black);
    white-space: nowrap;
  }
  .website svg { width: 26px; height: 26px; }

  .daughter-photo {
    position: absolute;
    left: 718px; top: 138px;
    width: 197px; height: 331px;
    border-radius: 90px 90px 10px 10px;
    background: linear-gradient(180deg, #e8c93a 0%, #e8c93a 10%, #c9a27e 18%, #d7c6ec 40%, #c7b3e6 75%, #8a8a8a 100%);
  }
</style>
</head>
<body>
  <section class="billboard">
    <div class="brand-mark">
      <span class="brand-square"></span>
      <span class="brand-name">HARLAN HOME SOLUTIONS</span>
    </div>

    <h1 class="company-title">HARLAN HOME SOLUTIONS</h1>
    <p class="slogan">BUILD – REPAIR – REPLACE</p>
    <p class="tagline">FOR ALL YOUR HOME<br>REMODEL NEEDS</p>

    <div class="phone">
      <svg viewBox="0 0 24 24" aria-hidden="true"><path fill="var(--phone-yellow)" d="M6.6 10.8c1.4 2.8 3.8 5.1 6.6 6.6l2.2-2.2c.3-.3.7-.4 1-.2 1.1.4 2.3.6 3.6.6.6 0 1 .4 1 1V20c0 .6-.4 1-1 1C10.6 21 3 13.4 3 4c0-.6.4-1 1-1h3.5c.6 0 1 .4 1 1 0 1.3.2 2.5.6 3.6.1.3 0 .7-.2 1z"/></svg>
      <span>555-014-2286</span>
    </div>

    <div class="web-band">
      <div class="website">
        <svg viewBox="0 0 24 24" aria-hidden="true"><g fill="none" stroke="var(--ink-black)" stroke-width="2"><circle cx="12" cy="12" r="9.5"/><ellipse cx="12" cy="12" rx="4.5" ry="9.5"/><path d="M2.5 12h19M4 7h16M4 17h16"/></g></svg>
        <span>www.harlanhomesolutions.com</span>
      </div>
    </div>

    <div class="daughter-photo" role="img" aria-label="Cut-out photo of a smiling young girl wearing a yellow hard hat and lavender puffer jacket, holding a hammer"></div>
  </section>
</body>
</html>
```